Business Card Design

We would like a business card that utilizes our current logo and keeps with the same feel - elegant and organic. Our farm isn't about mass production, it's about excellence, education, beautiful events and flowers - people, culture, and community.

Target Market(s)

Patrons to our farm who are interested in weddings, events, or our flowers and vegetables.

Contact Information for Business Card

Name, address, cell email (Danielle Hoskins, 2716 Wrenfield Rd, Alder Springs, MT 59990, cell 30.412.6638, email danielle@wrenfieldacres.com)

```html
<!DOCTYPE html>
<html lang="en">
<head>
<meta charset="utf-8">
<title>Wrenfield Acres — Business Card</title>
<link rel="stylesheet" href="https://fonts.googleapis.com/css2?family=Jost:wght@300&family=Questrial&display=swap">
<style>
  :root {
    --sage: #778a77;
    --paper: #fdfdfd;
    --canvas: #ffffff;
  }
  html, body {
    margin: 0;
    padding: 0;
    width: 1200px;
    height: 900px;
    overflow: hidden;
    background: var(--canvas);
  }
  .business-card {
    position: absolute;
    left: 318px;
    top: 273px;
    width: 569px;
    height: 357px;
    border-radius: 17px;
    background: var(--sage);
    overflow: hidden;
  }
  .identity-band {
    position: absolute;
    left: 0;
    top: 53px;
    width: 100%;
    height: 132px;
    background: var(--paper);
  }
  .brand-name {
    position: absolute;
    left: 34px;
    top: 0;
    width: 250px;
    height: 132px;
    display: flex;
    align-items: center;
    margin: 0;
    font-family: "Jost", sans-serif;
    font-weight: 300;
    font-size: 32px;
    line-height: 1.1;
    color: var(--sage);
    letter-spacing: 0.02em;
  }
  .person-name {
    position: absolute;
    right: 40px;
    top: 27px;
    margin: 0;
    text-align: right;
    font-family: "Jost", sans-serif;
    font-weight: 300;
    font-size: 34px;
    line-height: 37px;
    letter-spacing: 0.17em;
    margin-right: -0.17em;
    color: var(--sage);
    text-transform: uppercase;
  }
  .person-name span { display: block; }
  .contact-list {
    position: absolute;
    left: 31px;
    top: 222px;
    margin: 0;
    padding: 0;
    list-style: none;
  }
  .contact-item {
    display: flex;
    align-items: center;
    height: 26px;
    margin-bottom: 14px;
    font-family: "Questrial", sans-serif;
    font-size: 22px;
    color: var(--paper);
    letter-spacing: -0.01em;
    white-space: nowrap;
  }
  .contact-icon {
    width: 26px;
    height: 26px;
    margin-right: 10px;
    flex: none;
  }
</style>
</head>
<body>
  <article class="business-card">
    <section class="identity-band">
      <p class="brand-name">Wrenfield Acres</p>
      <h1 class="person-name"><span>Danielle</span><span>Hoskins</span></h1>
    </section>
    <ul class="contact-list">
      <li class="contact-item">
        <svg class="contact-icon" viewBox="0 0 26 26" aria-hidden="true">
          <rect width="26" height="26" rx="4" fill="var(--paper)"/>
          <path d="M13 4.5a6 6 0 0 0-6 6c0 4.5 6 11 6 11s6-6.5 6-11a6 6 0 0 0-6-6z" fill="var(--sage)"/>
          <circle cx="13" cy="10.5" r="2.3" fill="var(--paper)"/>
        </svg>
        2716 Wrenfield Rd, Alder Springs, MT 59990
      </li>
      <li class="contact-item">
        <svg class="contact-icon" viewBox="0 0 26 26" aria-hidden="true">
          <rect width="26" height="26" rx="4" fill="var(--paper)"/>
          <path d="M8.2 5.5l2.6 0.3 1.3 3.6-1.7 1.5c0.9 2 2.5 3.6 4.5 4.5l1.5-1.7 3.6 1.3 0.3 2.6-1.8 1.9C12.9 19.4 6.6 13.1 6.5 7.3z" fill="var(--sage)"/>
        </svg>
        30.412.6638
      </li>
      <li class="contact-item">
        <svg class="contact-icon" viewBox="0 0 26 26" aria-hidden="true">
          <rect width="26" height="26" rx="4" fill="var(--paper)"/>
          <rect x="5" y="7.5" width="16" height="11" fill="none" stroke="var(--sage)" stroke-width="1.6"/>
          <path d="M5 7.5l8 6.5 8-6.5M5 18.5l6-5.5M21 18.5l-6-5.5" fill="none" stroke="var(--sage)" stroke-width="1.4"/>
        </svg>
        danielle@wrenfieldacres.com
      </li>
    </ul>
  </article>
</body>
</html>
```